Website for new slot-booking/reservations website/software

For a new software product we need a brand new logo and website for a reservations/booking system. The website should ideally present the main features with information text, contact info, news page as well as registration and pricing pages. As currently primary field of operation the software should be used for tennis but later on, also for other sport types. Also we'd like to be the logo a text-brand which includes the name "feldreserve.com" or just "feldreserve". The logo should ideally include an icon-design in some way. Generally we are open for ideas.

Bootstrap 4 template is a minimum requirement. (Multi-Page preferred, Single-Page still OK.)

You can use the attached image as an inspiration, but change of colors or other design elements are up to you. Currently the application has a primary color of #5500ff. The website created by you will not include the application itself, so it can have different (but ideally similar) Look&Feel.

Target Market(s)

Sports, Club-Management

Logo Text

feldreserve.com

Coding

Coded - Design and coding required

Number of Pages Required

5+ page

Font styles to use
Sans Serif

Requirements
Must have
• Bootstrap 4 Template, SCSS
Nice to have
• Rapid Loading Times, not too much external JS Libraries.
Should not have
• Extensive animations

```html
<!DOCTYPE html>
<html lang="en">
<head>
<meta charset="utf-8">
<title>feldreserve – Booking System</title>
<link rel="stylesheet" href="https://fonts.googleapis.com/css2?family=Raleway:wght@300;400;500;600;700;800&display=swap">
<style>
  :root{
    --brand:#7540fb;
    --brand-deep:#5a40d2;
    --brand-dark:#2a1670;
    --cyan:#05d2ee;
    --cyan-soft:#e6fbfe;
    --pill:#efedf4;
    --ink:#14121c;
    --muted:#8a8799;
    --body:#3a3846;
    --white:#ffffff;
  }
  *{box-sizing:border-box;margin:0;padding:0}
  html,body{width:1200px;height:3907px;overflow:hidden}
  body{position:relative;background:var(--white);font-family:"Raleway",sans-serif;color:var(--ink)}
  .abs{position:absolute}

  /* nav */
  .brand{display:flex;align-items:center;gap:8px;font-weight:700;color:var(--brand)}
  .brand-dot{width:24px;height:24px;border-radius:50%;background:var(--brand)}
  .site-brand{left:104px;top:30px;font-size:26px}
  .nav-link{top:34px;font-size:18px;color:#4a4858;text-decoration:none}
  .nav-login{left:995px;top:29px;width:97px;height:33px;border:2px solid var(--brand-dark);border-radius:17px;font-size:16px;color:var(--brand-dark);display:flex;align-items:center;justify-content:center}

  /* hero */
  .hero-band{left:0;top:0}
  .hero-circle{left:143px;top:87px;width:418px;height:418px;border-radius:50%;background:var(--cyan)}
  .hero-photo{left:215px;top:108px;width:300px;height:544px;border-radius:140px 140px 0 0;background:linear-gradient(180deg,#6fb8ae 0%,#4f9d93 55%,#e9eef0 100%)}
  .hero-title{left:642px;top:262px;font-size:51px;font-weight:700;color:var(--white);letter-spacing:.5px;line-height:1}
  .hero-sub{left:642px;top:316px;font-size:31px;font-weight:500;color:var(--white);line-height:36px}
  .hero-lead{left:642px;top:393px;width:470px;font-size:21px;font-weight:400;color:#f0eaff;line-height:25px}
  .btn-hero{top:467px;height:41px;border-radius:21px;font-size:13px;font-weight:500;display:flex;align-items:center;justify-content:center}
  .btn-register{left:642px;width:130px;background:var(--white);color:var(--brand)}
  .btn-learn{left:792px;width:132px;border:2px solid var(--white);color:var(--white)}

  /* section labels */
  .pill{width:179px;height:44px;border-radius:22px;background:var(--pill);color:var(--brand);font-size:13px;display:flex;align-items:center;justify-content:center}
  .section-title{font-size:26px;font-weight:700;line-height:30px;color:var(--ink)}

  /* features */
  .feature-mockup{left:0;top:854px;width:542px;height:405px;border-radius:0 18px 8px 0;background:linear-gradient(135deg,#2b2b33 0%,#45434f 100%)}
  .feature-mockup::after{content:"";position:absolute;left:0;top:16px;right:24px;bottom:34px;background:linear-gradient(160deg,#ffffff 60%,#dcd6ff 100%)}
  .features-text{left:601px;top:843px;width:410px;font-size:17px;line-height:19px;color:var(--body)}
  .tick-box{width:31px;height:31px;border-radius:9px;background:var(--pill);display:flex;align-items:center;justify-content:center}
  .feature-title{width:230px;font-size:17px;font-weight:500;line-height:19px;color:var(--ink)}
  .feature-body{width:230px;font-size:17px;line-height:19px;color:var(--body)}

  /* about */
  .about-deco{left:857px;top:1430px;width:640px;height:640px;border-radius:50%;background:radial-gradient(circle at 35% 30%,#8b82ff 0%,#7a52fb 55%,#6a35f0 100%)}
  .about-text{left:99px;width:470px;font-size:27px;font-weight:300;line-height:29px;color:var(--body)}

  /* pricing */
  .plan{width:190px}
  .plan-price{font-size:30px;font-weight:700;color:var(--ink)}
  .plan-price span{font-size:14px;font-weight:400;color:var(--muted);margin-left:6px}
  .plan-name{margin-top:18px;font-size:23px;font-weight:600;color:var(--ink)}
  .plan-desc{margin-top:14px;font-size:12px;line-height:15px;color:var(--muted)}
  .plan-list{list-style:none;margin-top:16px}
  .plan-list li{display:flex;align-items:center;gap:9px;height:26px;font-size:12.5px;color:var(--muted)}
  .plan-list i{width:15px;height:15px;border-radius:50%;background:#e4e1f2;display:flex;align-items:center;justify-content:center}
  .plan-btn{margin-top:18px;width:172px;height:37px;border-radius:7px;background:var(--cyan-soft);color:var(--cyan);font-size:13px;font-weight:600;display:flex;align-items:center;justify-content:center}
  .plan-featured{left:587px;top:2253px;width:243px;height:399px;border-radius:10px;background:var(--brand-deep);box-shadow:0 30px 40px -20px rgba(90,64,210,.5);padding:18px 26px}
  .plan-featured .plan-price,.plan-featured .plan-name{color:var(--white)}
  .plan-featured .plan-price span,.plan-featured .plan-desc,.plan-featured .plan-list li{color:#e4defa}
  .plan-featured .plan-list i{background:#7c66e0}
  .plan-featured .plan-btn{width:192px;background:var(--cyan);color:#1a3d8a}
  .badge{margin-left:auto;width:99px;height:19px;border-radius:10px;background:#6e58de;color:#f3a9c0;font-size:9px;font-weight:700;letter-spacing:1px;display:flex;align-items:center;justify-content:center}

  /* news */
  .news-card{top:2916px;width:304px}
  .news-img{height:189px}
  .news-cat{margin-top:16px;font-size:12px;color:var(--brand)}
  .news-title{margin-top:4px;font-size:17px;font-weight:600;line-height:19px;color:var(--ink)}
  .news-body{margin-top:14px;width:270px;font-size:16px;line-height:19px;color:var(--body)}
  .news-date{margin-top:6px;display:flex;align-items:center;gap:8px;font-size:10px;color:var(--muted)}
  .news-date i{width:13px;height:12px;border:1.5px solid #b9b0ee;border-radius:2px}
  .news-btn{margin-top:12px;width:172px;height:36px;border-radius:8px;background:#ece8fc;color:var(--brand);font-size:13px;font-weight:600;display:flex;align-items:center;justify-content:center}

  /* footer */
  .footer-wave{left:0;top:3410px}
  .footer-brand{left:88px;top:3582px;font-size:32px;color:var(--white);font-weight:600}
  .footer-brand .brand-dot{width:32px;height:32px;background:var(--white)}
  .footer-tag{left:88px;top:3633px;width:470px;font-size:19px;font-weight:500;line-height:25px;color:#a899ff}
  .footer-head{top:3579px;font-size:15px;font-weight:600;color:#a295ff}
  .footer-list{top:3636px;list-style:none;font-size:15px;line-height:24px;color:var(--white)}
  .footer-copy{left:88px;top:3828px;font-size:13px;color:#c6a9f2}
  .footer-terms{left:998px;top:3828px;font-size:14px;font-weight:700;color:var(--white)}
</style>
</head>
<body>

<!-- navigation -->
<div class="abs brand site-brand"><span class="brand-dot"></span>feldreserve</div>
<span class="abs nav-link" style="left:602px">Home</span>
<span class="abs nav-link" style="left:699px">Templates</span>
<span class="abs nav-link" style="left:831px">Price</span>
<span class="abs nav-link" style="left:921px">Help</span>
<div class="abs nav-login">Login</div>

<!-- hero -->
<svg class="abs hero-band" width="1200" height="660" viewBox="0 0 1200 660">
  <path d="M0 142 L510 150 C540 151 560 158 600 162 L1188 176 Q1198 176 1198 188 L1198 652 L10 652 Q0 652 0 642 Z" fill="var(--brand)"/>
</svg>
<div class="abs hero-circle"></div>
<div class="abs hero-photo" role="img" aria-label="Photo of a tennis player holding a racket"></div>
<div class="abs hero-title">BOOKING SYSTEM</div>
<div class="abs hero-sub">FOR SPORTS, GYMS,<br>CLASSES AND MORE</div>
<div class="abs hero-lead">Easy to use and customisable online booking system you can trust</div>
<div class="abs btn-hero btn-register">Register now</div>
<div class="abs btn-hero btn-learn">Learn more</div>

<!-- features -->
<div class="abs feature-mockup" role="img" aria-label="Laptop showing the pricing page of the booking app"></div>
<div class="abs pill" style="left:601px;top:704px">FEATURES</div>
<h2 class="abs section-title" style="left:601px;top:768px">Online Booking System for<br>Individual Reservations</h2>
<p class="abs features-text">The system allows one booking during the time. It is possible to set-up different prices based on peak or off-peak periods. The system uses different colours, where colours can be different for each person or booking status.</p>

<div class="abs tick-box" style="left:602px;top:975px"><svg width="14" height="10" viewBox="0 0 14 10"><path d="M1 5l4 4 8-8" fill="none" stroke="var(--brand)" stroke-width="1.6"/></svg></div>
<div class="abs feature-title" style="left:602px;top:1027px">Better Management of Multi-Function Halls</div>
<div class="abs feature-body" style="left:602px;top:1082px">Multi-function halls; for example, a hall can be used for the</div>

<div class="abs tick-box" style="left:872px;top:975px"><svg width="14" height="10" viewBox="0 0 14 10"><path d="M1 5l4 4 8-8" fill="none" stroke="var(--brand)" stroke-width="1.6"/></svg></div>
<div class="abs feature-title" style="left:872px;top:1027px">Better Management of Multi-Function Halls</div>
<div class="abs feature-body" style="left:872px;top:1082px">Multi-function halls; for example, a hall can be used for the</div>

<div class="abs tick-box" style="left:604px;top:1168px"><svg width="14" height="10" viewBox="0 0 14 10"><path d="M1 5l4 4 8-8" fill="none" stroke="var(--brand)" stroke-width="1.6"/></svg></div>
<div class="abs feature-title" style="left:604px;top:1220px">Better Management of Multi-Function Halls</div>
<div class="abs feature-body" style="left:604px;top:1274px">Multi-function halls; for example, a hall can be used for the</div>

<div class="abs tick-box" style="left:874px;top:1168px"><svg width="14" height="10" viewBox="0 0 14 10"><path d="M1 5l4 4 8-8" fill="none" stroke="var(--brand)" stroke-width="1.6"/></svg></div>
<div class="abs feature-title" style="left:874px;top:1220px">Better Management of Multi-Function Halls</div>
<div class="abs feature-body" style="left:874px;top:1274px">Multi-function halls; for example, a hall can be used for the</div>

<!-- about -->
<div class="abs about-deco"></div>
<div class="abs pill" style="left:99px;top:1461px">feldreserve</div>
<h2 class="abs section-title" style="left:99px;top:1525px">About feldreserve<br>Booking System</h2>
<p class="abs about-text" style="top:1608px">feldreserve booking system has been created to help gyms, sport centres and other businesses to manage bookings online. It can be used to manage creche in gyms, group activities or individual sports like badminton or tennis.</p>
<p class="abs about-text" style="top:1810px">Our system is easy to use for both business owners and end-users. We have a wide range of settings that customise system to your needs. You can check out some of our testimonials.</p>

<!-- pricing -->
<div class="abs pill" style="left:111px;top:2066px">Pricing</div>
<h2 class="abs section-title" style="left:111px;top:2130px">Find the perfect plan that<br>fits for you.</h2>

<div class="abs plan" style="left:144px;top:2328px">
  <div class="plan-price">$20<span>/month</span></div>
  <div class="plan-name">Intro</div>
  <div class="plan-desc">For most businesses that want to otpimize web queries</div>
  <ul class="plan-list">
    <li><i></i>All limited links</li><li><i></i>Own analytics platform</li><li><i></i>Chat support</li><li><i></i>Optimize hashtags</li><li><i></i>Unlimited users</li>
  </ul>
  <div class="plan-btn">Choose plan</div>
</div>

<div class="abs plan" style="left:366px;top:2328px">
  <div class="plan-price">$50<span>/month</span></div>
  <div class="plan-name">Base</div>
  <div class="plan-desc">For most businesses that want to otpimize web queries</div>
  <ul class="plan-list">
    <li><i></i>All limited links</li><li><i></i>Own analytics platform</li><li><i></i>Chat support</li><li><i></i>Optimize hashtags</li><li><i></i>Unlimited users</li>
  </ul>
  <div class="plan-btn">Choose plan</div>
</div>

<div class="abs plan-featured">
  <div class="badge">MOST POPULAR</div>
  <div class="plan-price" style="margin-top:6px">$100<span>/month</span></div>
  <div class="plan-name" style="margin-top:20px">Pro</div>
  <div class="plan-desc" style="margin-top:12px">For most businesses that want to otpimize web queries</div>
  <ul class="plan-list" style="margin-top:14px">
    <li><i></i>All limited links</li><li><i></i>Own analytics platform</li><li><i></i>Chat support</li><li><i></i>Optimize hashtags</li><li><i></i>Unlimited users</li>
  </ul>
  <div class="plan-btn" style="margin-top:16px">Choose plan</div>
</div>

<div class="abs plan" style="left:859px;top:2328px">
  <div class="plan-price">$200<span>/month</span></div>
  <div class="plan-name">Enterprise</div>
  <div class="plan-desc">For most businesses that want to otpimize web queries</div>
  <ul class="plan-list">
    <li><i></i>All limited links</li><li><i></i>Own analytics platform</li><li><i></i>Chat support</li><li><i></i>Optimize hashtags</li><li><i></i>Unlimited users</li>
  </ul>
  <div class="plan-btn">Choose plan</div>
</div>

<!-- news -->
<div class="abs pill" style="left:111px;top:2732px">News</div>
<h2 class="abs section-title" style="left:111px;top:2796px">Leatest updates on the<br>booking/system</h2>

<article class="abs news-card" style="left:99px">
  <div class="news-img" role="img" aria-label="Photo of joined hands in teamwork" style="background:linear-gradient(135deg,#c79a7c,#e7d9d0 60%,#b9c9e4)"></div>
  <div class="news-cat">TRAININGS</div>
  <div class="news-title">Better Management of<br>Multi-Function Halls</div>
  <p class="news-body">Multi-function halls; for example, a hall can be used for the whole court of basketball or 2 courts of badminton...</p>
  <div class="news-date"><i></i>May 12, 2021</div>
  <div class="news-btn">Read more</div>
</article>

<article class="abs news-card" style="left:456px">
  <div class="news-img" role="img" aria-label="Photo of a team meeting in a modern office" style="background:linear-gradient(135deg,#b98a62,#6f6a6c 55%,#9aa6b5)"></div>
  <div class="news-cat">TRAININGS</div>
  <div class="news-title">Better Management of<br>Multi-Function Halls</div>
  <p class="news-body">Multi-function halls; for example, a hall can be used for the whole court of basketball or 2 courts of badminton...</p>
  <div class="news-date"><i></i>May 12, 2021</div>
  <div class="news-btn">Read more</div>
</article>

<article class="abs news-card" style="left:793px">
  <div class="news-img" role="img" aria-label="Photo of people on a rooftop terrace" style="background:linear-gradient(135deg,#c9c2b8,#8e8a84 50%,#6f8f5a)"></div>
  <div class="news-cat">TRAININGS</div>
  <div class="news-title">Better Management of<br>Multi-Function Halls</div>
  <p class="news-body">Multi-function halls; for example, a hall can be used for the whole court of basketball or 2 courts of badminton...</p>
  <div class="news-date"><i></i>May 12, 2021</div>
  <div class="news-btn">Read more</div>
</article>

<!-- footer -->
<svg class="abs footer-wave" width="1200" height="497" viewBox="0 0 1200 497">
  <defs>
    <linearGradient id="footerGrad" x1="0" y1="0" x2="0" y2="1">
      <stop offset="0" stop-color="#6a5ef7"/>
      <stop offset="1" stop-color="#7a2fc9"/>
    </linearGradient>
  </defs>
  <path d="M0 95 C120 40 230 0 360 20 C480 40 560 150 720 135 C880 120 1000 10 1200 2 L1200 497 L0 497 Z" fill="url(#footerGrad)"/>
</svg>
<div class="abs brand footer-brand"><span class="brand-dot"></span>feldreserve</div>
<p class="abs footer-tag">Feldreserve is the first joint human and AI business with a dedication to developing.</p>

<div class="abs footer-head" style="left:613px">Links</div>
<ul class="abs footer-list" style="left:613px"><li>About us</li><li>Servcies</li><li>Demo</li><li>Contact</li></ul>

<div class="abs footer-head" style="left:789px">Reach us</div>
<ul class="abs footer-list" style="left:789px;top:3630px"><li>www.courtlane.com</li><li>info@courtlane.com</li><li>Tel: +64 4 555 0192</li></ul>

<div class="abs footer-head" style="left:965px">Resources</div>
<ul class="abs footer-list" style="left:963px"><li>Customer portal</li></ul>

<div class="abs footer-copy">© 2020-2021 All Rights Reserved.</div>
<div class="abs footer-terms">Terms of Service</div>

</body>
</html>
```